Effectively Manage Muscular Pain /with Remedial Massage

A flyer to sell remedial massage Therapy for muscular pain .

$10 Discount with this flyer

Use colors orange and Blak with the color of the logo provided and preferably the fonts as well .

Little spin about remedial massage:

Remedial massage is a deep massage , to create the conditions for the body’s return to normal health after injury or with muscular-skeletal disorders. It is used to treat chronic muscular-skeletal imbalances, strains, sprains, broken bones, bruising or any injury. Deep tissue massage removes blockages, damaged cells, scar tissue and adhesions [speeds up recovery Remedial massage is also used for conditions created by lifestyle for example Repetitive strain injury and Back pain.

Target Market(s)

young professionals with kids , modern suburban couples

Industry/Entity Type

Massage

Requirements
Must have
• doble sided.

Address 418 tindall Rd , Footscray Book Now 96402873

```html
<!DOCTYPE html>
<html lang="en">
<head>
<meta charset="utf-8">
<title>Remedial Massage Flyer – Front and Back</title>
<link rel="stylesheet" href="https://fonts.googleapis.com/css2?family=Oswald:wght@400;700&family=Open+Sans:wght@400;600&display=swap">
<style>
  :root{
    --orange:#f0561e;
    --orange-deep:#e0401a;
    --black:#0b0b0b;
    --ink:#1c1c1c;
    --band:#262626;
    --white:#ffffff;
    --page:#f4f4f4;
    --grey:#8a8a8a;
  }
  *{box-sizing:border-box;margin:0;padding:0}
  html,body{width:1200px;height:1184px;overflow:hidden}
  body{background:var(--page);position:relative;font-family:"Open Sans",Arial,sans-serif}

  .flyer{position:absolute;top:97px;width:540px;height:990px;overflow:hidden;
    background:radial-gradient(ellipse at 50% 30%,#3a3a3a 0%,var(--ink) 45%,var(--black) 100%);
    box-shadow:0 6px 24px rgba(0,0,0,.25)}
  .flyer--front{left:40px}
  .flyer--back{left:620px}

  /* brand block */
  .brand{position:absolute;display:flex;align-items:center}
  .brand__dot{border-radius:50%;border:solid var(--orange);flex:none}
  .brand__name{font-family:"Oswald",Arial,sans-serif;font-weight:400;color:var(--white);text-transform:uppercase;line-height:1.05}

  .front-brand{left:24px;top:28px}
  .front-brand .brand__dot{width:118px;height:118px;border-width:14px;background:var(--black)}
  .front-brand .brand__name{font-size:42px;margin-left:22px;letter-spacing:.5px}

  .address-band{position:absolute;left:0;right:0;top:150px;height:40px;background:var(--orange);
    font-family:"Oswald",Arial,sans-serif;font-weight:700;font-size:24px;color:var(--black);
    text-align:right;padding-right:26px;line-height:40px}

  .headline{position:absolute;left:0;right:0;top:196px;text-align:center;font-family:"Oswald",Arial,sans-serif;
    font-weight:700;font-size:60px;color:var(--orange);line-height:1.1}
  .subline{position:absolute;left:0;right:0;top:270px;text-align:center;color:var(--white);font-size:25px}

  .photo-back-pain{position:absolute;left:0;right:0;top:320px;height:430px;
    background:radial-gradient(ellipse at 45% 55%,rgba(220,40,40,.55) 0%,rgba(120,120,120,.35) 30%,rgba(40,40,40,0) 65%),
               linear-gradient(180deg,#2a2a2a 0%,#5a5a5a 55%,#1e1e1e 100%)}

  /* coupon */
  .coupon{position:absolute;left:26px;right:26px;height:176px;border:3px dashed var(--orange);border-radius:26px;
    display:flex;align-items:center}
  .coupon__scissors{position:absolute;top:-12px;left:50%;transform:translateX(-50%);background:var(--black);padding:0 6px}
  .coupon__offer{width:44%;text-align:center;color:var(--white)}
  .coupon__amount{font-family:"Oswald",Arial,sans-serif;font-weight:700;color:var(--orange-deep);font-size:72px;line-height:1}
  .coupon__amount small{font-size:34px}
  .coupon__note{font-size:22px}
  .coupon__divider{width:2px;height:120px;background:#444}
  .coupon__brand{flex:1;padding-left:18px}
  .coupon .brand{position:static}
  .coupon .brand__dot{width:64px;height:64px;border-width:8px;background:var(--black)}
  .coupon .brand__name{font-size:24px;margin-left:12px}
  .coupon__service{color:var(--orange);font-size:16px;text-align:center;margin-top:8px;line-height:1.25}
  .flyer--front .coupon{top:775px}
  .flyer--back .coupon{top:780px}

  /* back */
  .photo-woman{position:absolute;left:0;top:0;width:200px;height:288px;
    background:linear-gradient(160deg,#c9a27a 0%,#d8b89a 35%,#9fb6d6 70%,#2a2a2a 100%)}
  .relief{position:absolute;left:170px;right:0;top:120px;height:160px;background:var(--orange);padding:14px 10px 0;text-align:center}
  .relief__title{font-family:"Oswald",Arial,sans-serif;font-weight:700;font-size:42px;color:var(--black);line-height:1.1;white-space:nowrap}
  .relief__list{color:var(--white);font-size:19px;line-height:1.3;margin-top:6px}
  .intro{position:absolute;left:24px;right:24px;top:298px;text-align:center;color:var(--orange);font-size:19px;line-height:1.3}

  .point{position:absolute;left:0;right:0;text-align:center;color:var(--white);font-size:20px;line-height:1.3;
    background:linear-gradient(180deg,var(--band) 0%,#151515 100%);display:flex;align-items:center;justify-content:center;padding:0 30px}
  .point--blockages{top:400px;height:80px}
  .point--recovery{top:500px;height:52px}
  .point--lifestyle{top:572px;height:112px}
  .arrow{position:absolute;left:50%;transform:translateX(-50%);width:0;height:0;
    border-left:11px solid transparent;border-right:11px solid transparent;border-top:14px solid var(--orange);z-index:2}
  .arrow--1{top:390px}.arrow--2{top:488px}.arrow--3{top:560px}

  .cta{position:absolute;left:0;right:0;top:696px;text-align:center;font-family:"Oswald",Arial,sans-serif;
    font-weight:700;font-size:50px;color:var(--orange);line-height:1.1}
</style>
</head>
<body>

<section class="flyer flyer--front" aria-label="Flyer front">
  <div class="brand front-brand">
    <span class="brand__dot"></span>
    <span class="brand__name">Renwick Osteopathy<br>Clinical Pilates</span>
  </div>
  <div class="address-band">418 tindall Rd , Footscray</div>
  <h1 class="headline">Remedial Massage</h1>
  <p class="subline">for that pesky back pain</p>
  <div class="photo-back-pain" role="img" aria-label="Photo of a hand pressing on a sore lower back with a red glow"></div>

  <div class="coupon">
    <svg class="coupon__scissors" width="34" height="20" viewBox="0 0 34 20" aria-hidden="true">
      <circle cx="6" cy="5" r="4" fill="none" stroke="#f0561e" stroke-width="2"/>
      <circle cx="6" cy="15" r="4" fill="none" stroke="#f0561e" stroke-width="2"/>
      <path d="M9 7 L30 16 M9 13 L30 4" stroke="#f0561e" stroke-width="2"/>
    </svg>
    <div class="coupon__offer">
      <div class="coupon__amount">$10<small>off</small></div>
      <div class="coupon__note">with this flyer</div>
    </div>
    <div class="coupon__divider"></div>
    <div class="coupon__brand">
      <div class="brand"><span class="brand__dot"></span><span class="brand__name">Renwick Osteopathy<br>Clinical Pilates</span></div>
      <p class="coupon__service">Remedial Massage Therapy<br>for muscular pain</p>
    </div>
  </div>
</section>

<section class="flyer flyer--back" aria-label="Flyer back">
  <div class="photo-woman" role="img" aria-label="Photo of a woman holding her sore neck"></div>
  <div class="relief">
    <h2 class="relief__title">Relief from PAIN</h2>
    <p class="relief__list">strains, sprains, broken bones,<br>bruising or any injury</p>
  </div>
  <p class="intro">Remedial massage is a deep massage , to create the conditions for the body’s return to normal health after injury or with muscular-skeletal disorders.</p>

  <span class="arrow arrow--1"></span>
  <p class="point point--blockages">Removes blockages, damaged cells, scar tissue and adhesions</p>
  <span class="arrow arrow--2"></span>
  <p class="point point--recovery">Speeds up recovery</p>
  <span class="arrow arrow--3"></span>
  <p class="point point--lifestyle">Remedial massage is also used for conditions created by lifestyle for example repetitive strain injury and Back pain.</p>

  <h2 class="cta">Avail Discount TODAY!</h2>

  <div class="coupon">
    <svg class="coupon__scissors" width="34" height="20" viewBox="0 0 34 20" aria-hidden="true">
      <circle cx="6" cy="5" r="4" fill="none" stroke="#f0561e" stroke-width="2"/>
      <circle cx="6" cy="15" r="4" fill="none" stroke="#f0561e" stroke-width="2"/>
      <path d="M9 7 L30 16 M9 13 L30 4" stroke="#f0561e" stroke-width="2"/>
    </svg>
    <div class="coupon__offer">
      <div class="coupon__amount">$10<small>off</small></div>
      <div class="coupon__note">with this flyer</div>
    </div>
    <div class="coupon__divider"></div>
    <div class="coupon__brand">
      <div class="brand"><span class="brand__dot"></span><span class="brand__name">Renwick Osteopathy<br>Clinical Pilates</span></div>
      <p class="coupon__service">Remedial Massage Therapy<br>for muscular pain</p>
    </div>
  </div>
</section>

</body>
</html>
```